Glenvora pond linings website template

We need a template for our new website. Glenvora is currently marketed through www.sheetvale.com.au, and we are moving the pond/dam linings to a dedicated site www.glenvora.com.au

The site is essentially brochureware. The content (less landing page & photo gallery) is on the new site to give you a better idea of what we do. We are also on Facebook.com/glenvora

We are looking for a template/style which we can adapt to the different sections of the site as required. We also get a lot of phone/tablet visitors so an alternative mobile layout would be a bonus, but by no means required.

I am proficient in HTML/CSS & javascript so can code most designs thrown at me.

Any icons or interface fonts should be freely available web fonts where possible.

Target Market(s)

We are targeting both landscape professionals (design & construction) as well as the DIY market for ponds/wateragrdens.

Industry/Entity Type

Moving

Requirements
Must have
• We need a design (preferably layered PSD or AI) as basis for our overall site look and feel. Fonts/iconography/layout are where we are lacking. We can do the HTML/CSS/JS/PHP internally.
Nice to have
• A style guide either in file or separate would be nice.
Layers with effect (i.e.. :hover, CSS3 transition endpoints, etc)

```html
<!DOCTYPE html>
<html lang="en">
<head>
<meta charset="utf-8">
<title>Glenvora – Custom made liners for ponds, pools &amp; watergardens</title>
<link rel="stylesheet" href="https://fonts.googleapis.com/css2?family=Raleway:wght@300;400;500;700&display=swap">
<style>
:root{
  --lime-top:#c2ff45;
  --white:#ffffff;
  --band:#ebfd6c;
  --band-edge:#c9d84a;
  --band-fold:#a8b43a;
  --ink-dark:#1f4a0c;
  --ink:#3d5f14;
  --ink-soft:#6c9c2c;
  --card:#e6f0d3;
  --footer:#dcff8e;
  --button:#e7fd4e;
  --dot-on:#8fc43a;
  --brand:#0f6a43;
}
*{margin:0;padding:0;box-sizing:border-box}
html,body{width:1200px;height:1172px;overflow:hidden}
body{
  position:relative;
  font-family:"Raleway",Arial,sans-serif;
  color:var(--ink);
  background:linear-gradient(to bottom,var(--lime-top) 0px,#e9ffc0 560px,var(--white) 1000px);
}
.page{position:absolute;left:79px;top:16px;width:1056px;height:1096px;background:var(--white)}

/* header */
.brand{position:absolute;left:99px;top:60px;display:flex;align-items:center;gap:14px}
.brand-mark{width:46px;height:46px;background:var(--brand)}
.brand-name{font-size:46px;font-weight:500;color:var(--brand);letter-spacing:2px;line-height:1}
.tagline{position:absolute;right:84px;top:29px;font-size:29px;font-weight:300;color:var(--ink-soft);white-space:nowrap;text-align:right;line-height:1.2}
.search{position:absolute;left:829px;top:124px;display:flex;align-items:center}
.search-label{font-size:16px;color:var(--ink);margin-right:11px}
.search-field{width:188px;height:26px;border:1px solid #c9d99a;border-radius:5px 0 0 5px;background:#fff}
.search-button{width:42px;height:26px;background:var(--button);border-radius:0 5px 5px 0;display:flex;align-items:center;justify-content:center}

/* bands */
.band{position:absolute;left:67px;width:1079px;background:var(--band);border-top:1px solid var(--band-edge);border-bottom:1px solid var(--band-edge)}
.band::before,.band::after{content:"";position:absolute;bottom:-6px;border-top:6px solid var(--band-fold)}
.band::before{left:0;border-left:12px solid transparent}
.band::after{right:0;border-right:12px solid transparent}
.nav{top:163px;height:38px}
.nav ul{list-style:none;display:flex;justify-content:center;align-items:center;height:100%;padding-left:6px}
.nav li{font-size:15.8px;color:var(--ink-dark);text-transform:uppercase;white-space:nowrap}
.nav li+li::before{content:"|";margin:0 12px;color:var(--ink)}
.pager{top:514px;height:26px}
.dots{display:flex;gap:9px;justify-content:center;padding-top:4px}
.dots span{width:15px;height:15px;border-radius:50%;background:#fff}
.dots span.active{background:var(--dot-on)}

/* slider */
.slider{position:absolute;left:79px;top:201px;width:1056px;height:313px;
  background:linear-gradient(100deg,#4f7d2c 0%,#8ea47a 30%,#7b7c72 48%,#c8cbc4 58%,#6d7064 68%,#3f5e2a 82%,#2c4a1a 100%)}
.slide-panel{position:absolute;left:51px;top:12px;width:389px;height:282px;background:rgba(255,255,255,.42);padding:40px 15px 0}
.slide-panel h1{font-size:27px;font-weight:700;color:#1a1a10}
.slide-panel p{font-size:20px;line-height:24px;color:#1a1a10;margin-top:18px}
.slide-action{display:inline-block;margin-top:32px;background:var(--button);border-radius:5px;padding:3px 8px;font-size:17px;font-weight:700;color:#1a1a10;box-shadow:0 1px 3px rgba(0,0,0,.35)}
.slide-arrow{position:absolute;top:130px}
.slide-arrow.prev{left:13px}
.slide-arrow.next{right:11px}

/* cards */
.card{position:absolute;top:564px;width:312px;height:301px;background:var(--card);border-radius:5px}
.card h2{position:absolute;left:9px;top:9px;font-size:19px;font-weight:700;color:var(--ink-dark)}
.card-image{position:absolute;left:10px;top:43px;width:292px;height:148px}
.card p{position:absolute;left:10px;top:199px;width:292px;font-size:14px;line-height:16.3px;text-align:justify;text-align-last:left;color:var(--ink-dark)}
.card-1{left:124px}.card-2{left:451px}.card-3{left:778px}
.card-1 .card-image{background:linear-gradient(160deg,#b9c6cf 0%,#8a7a5f 45%,#4f5a3a 100%)}
.card-2 .card-image{background:linear-gradient(160deg,#b6c0c2 0%,#b0533a 45%,#3e7a2a 100%)}
.card-3 .card-image{background:linear-gradient(160deg,#c9d2c8 0%,#6f7a5e 40%,#a9b64a 100%)}

.note{position:absolute;left:125px;top:897px;width:966px;height:65px;background:var(--card);border-radius:4px;display:flex;align-items:center;justify-content:center;font-size:19px;color:var(--ink)}

/* footer */
.footer{position:absolute;left:79px;top:989px;width:1056px;height:123px;background:var(--footer)}
.address{position:absolute;left:57px;top:30px;font-size:13.5px;line-height:16.5px;font-style:normal;color:var(--ink)}
.follow{position:absolute;right:56px;top:24px;text-align:right}
.follow-label{font-size:14px;color:var(--ink-dark)}
.social{display:flex;gap:10px;margin-top:4px}
.social span{width:43px;height:45px;border-radius:7px;background:#3f8a1f;box-shadow:0 1px 3px rgba(0,0,0,.3)}
</style>
</head>
<body>
<div class="page"></div>

<header>
  <div class="brand"><span class="brand-mark"></span><span class="brand-name">Glenvora</span></div>
  <p class="tagline">Custom made liners for ponds, pools &amp; watergardens.</p>
  <div class="search">
    <span class="search-label">Search</span>
    <span class="search-field"></span>
    <span class="search-button">
      <svg width="22" height="14" viewBox="0 0 22 14"><circle cx="7" cy="6" r="4.5" fill="none" stroke="#7a8a2a" stroke-width="2"/><line x1="10.5" y1="8" x2="18" y2="12" stroke="#7a8a2a" stroke-width="3" stroke-linecap="round"/></svg>
    </span>
  </div>
</header>

<nav class="band nav">
  <ul>
    <li>Home</li><li>About us</li><li>Happenings</li><li>Gallery</li><li>Liner styles</li><li>Preparation</li><li>Instalation</li><li>Contact us</li>
  </ul>
</nav>

<section class="slider" role="img" aria-label="Photo of a garden waterfall cascading over rocks among ferns">
  <div class="slide-panel">
    <h1>Heading 1</h1>
    <p>Lorem ipsum dolor sit amet, consectetur adipiscing elit. Cras imperdiet enim ac augue auctor viverra.</p>
    <span class="slide-action">Action 1</span>
  </div>
  <svg class="slide-arrow prev" width="26" height="51" viewBox="0 0 26 51"><polygon points="26,0 0,25.5 26,51" fill="#d9f96a"/></svg>
  <svg class="slide-arrow next" width="26" height="51" viewBox="0 0 26 51"><polygon points="0,0 26,25.5 0,51" fill="#d9f96a"/></svg>
</section>

<div class="band pager"><div class="dots"><span class="active"></span><span></span><span></span><span></span></div></div>

<article class="card card-1">
  <h2>Header 1</h2>
  <div class="card-image" role="img" aria-label="Photo of a house garden with a timber deck beside a pond"></div>
  <p>Lorem ipsum dolor sit amet, consectetur adipiscing elit.<br>Cras imperdiet enim ac augue auctor viverra. Lorem ipsum dolor sit amet, consectetur adipiscing elit.</p>
</article>
<article class="card card-2">
  <h2>Header 2</h2>
  <div class="card-image" role="img" aria-label="Photo of a red metal garden sculpture among ferns"></div>
  <p>Lorem ipsum dolor sit amet, consectetur adipiscing elit.<br>Cras imperdiet enim ac augue auctor viverra. Lorem ipsum dolor sit amet, consectetur adipiscing elit.</p>
</article>
<article class="card card-3">
  <h2>Header 3</h2>
  <div class="card-image" role="img" aria-label="Photo of a natural pond edged with rocks and flowering plants"></div>
  <p>Lorem ipsum dolor sit amet, consectetur adipiscing elit.<br>Cras imperdiet enim ac augue auctor viverra. Lorem ipsum dolor sit amet, consectetur adipiscing elit.</p>
</article>

<p class="note">Lorem ipsum dolor sit amet, consectetur adipiscing elit. Cras imperdiet enim ac augue auctor viverra.</p>

<footer class="footer">
  <address class="address">Unit 4, 12-16 Larkfield Way,<br>Brookdale, Victoria,<br>Australia 3099<br>phone +61 1300 555 018</address>
  <div class="follow">
    <div class="follow-label">Follow us:</div>
    <div class="social"><span aria-label="Social page 1"></span><span aria-label="Social page 2"></span></div>
  </div>
</footer>
</body>
</html>
```